Label Sticker Design for Apothecary Brand

Hello! We are an independent grassroots business located in Ontario, Canada that specializes in making organic botanical and herbal skin care, tea, witchcraft and wellness products. We have been in business for 5 years and are looking to create a label sticker with one of our slogans for use in packaging.

Our brand is dark, herbal, witchy, and modern with old-world apothecary and vintage influences. We want a label that will be VERY clean, and easily explain what our product is, while conveying a sense of mysticism and magic, as well as a traditional apothecary vibe.

We have attached design inspiration to give you an idea of the style that we would like. Our demographic is hipster, current, (think finger tattoos, linen dresses, and organic groceries), and they care deeply about where we source our ingredients, and how we craft our product. We don't want an old-school sticker that looks like it should be on the shelves of a health food store. The design should be contemporary, upmarket, modern and clean, but evoke a strong sense of magic and self-care with wild gathered herbs and unusual wild flowers!

This will be used as a packaging sticker for our shipping boxes.

We look forward to your winning design!
Thank you very much.

Target Market(s)

20 - 50yr Female Demographic
Natural, bohemian, earthy, hipster and modern

Key Words: Minimalist Tattoos, Organic Skin Care, Bohemian, Witchy, Dark, Moody, Confident, Sustainable, Ethical,

PLEASE VIEW PHOTOS BEFORE SUBMITTING A DESIGN ;)

Industry/Entity Type

Skin Care Product

Font styles to use
Serif
Script

Colors
1b1b1b
5c5c5c
fbfbfb

Requirements
Must have
• Clean and Simple - Take a look at the photos we've posted!
• Black / greyscale (No color)
• Label sticker must be a rectangle (3" x 2")
• Very Modern with a touch of old-world
• We are open to a variety of font styles. Please see photo FONT in image files, or the images 'Bottle Inspiration'
• Please use the following text:
• Thornmoor Stillhouse
• --------------------
• Crafted with Magic
• * Once your design is chosen and purchased, we will require the names of all fonts and sources of imagery used.
Nice to have
• A moody botanical graphic surrounding the text. Tangled wild, antique botanical illustrations. Not mandatory, but would be very nice.
Should not have
• Colour
• Messy or overly dramatic fonts
• Cartoon Imagery
• Leaf Motif
• Female Body Silhouettes
• Scroll or decorative borders.
• Butterflies, birds etc
• Actual pictures of witches
• Mandalas or Messy Graphics

```html
<!DOCTYPE html>
<html lang="en">
<head>
<meta charset="UTF-8">
<title>Thornmoor Stillhouse – Label Sticker</title>
<link rel="stylesheet" href="https://fonts.googleapis.com/css2?family=Inconsolata:wght@400;500&family=Great+Vibes&family=Open+Sans:wght@400&display=swap">
<style>
  :root {
    --ink: #000000;
    --charcoal: #1b1b1b;
    --grey: #5c5c5c;
    --line-grey: #8a8a8a;
    --paper: #ffffff;
    --snow: #fbfbfb;
    --title-fill-light: #f5f9fc;
  }
  * { margin: 0; padding: 0; box-sizing: border-box; }
  html, body {
    width: 829px; height: 1200px; overflow: hidden;
    background: var(--paper);
  }
  .canvas { position: relative; width: 829px; height: 1200px; background: var(--paper); }

  .label {
    position: absolute; left: 65px; width: 696px; height: 502px;
  }
  .label--dark { top: 52px; background: var(--ink); color: var(--snow); }
  .label--light { top: 625px; background: var(--paper); color: var(--ink); border: 1px solid #cfcfcf; }

  .botanical-wreath {
    position: absolute; left: 65px; top: 71px; width: 569px; height: 207px;
    border-radius: 50% / 45%;
  }
  .label--dark .botanical-wreath {
    background: radial-gradient(ellipse at center, rgba(190,190,190,0.38) 0%, rgba(150,150,150,0.2) 55%, rgba(0,0,0,0) 75%);
  }
  .label--light .botanical-wreath {
    background: radial-gradient(ellipse at center, rgba(110,110,110,0.32) 0%, rgba(140,140,140,0.16) 55%, rgba(255,255,255,0) 75%);
  }

  .brand-plate {
    position: absolute; left: 142px; top: 127px; width: 415px; height: 70px;
    display: flex; align-items: center; justify-content: center;
    font-family: "Inconsolata", monospace; font-weight: 500;
    font-size: 32px; letter-spacing: 3px; text-transform: uppercase;
  }
  .label--dark .brand-plate { background: var(--ink); border: 5px solid var(--snow); color: var(--snow); }
  .label--light .brand-plate { background: var(--title-fill-light); border: 4px solid var(--ink); color: var(--ink); }

  .slogan-row {
    position: absolute; left: 0; right: 0; display: flex; align-items: center; justify-content: center;
  }
  .label--dark .slogan-row { top: 325px; }
  .label--light .slogan-row { top: 325px; }
  .rule { height: 1px; background: var(--line-grey); }
  .label--dark .rule { width: 222px; }
  .label--dark .rule--left { margin-right: auto; }
  .label--dark .rule--right { margin-left: auto; }
  .label--light .rule { width: 88px; background: var(--grey); }
  .slogan {
    font-family: "Great Vibes", cursive; font-size: 27px; line-height: 36px;
    padding: 0 18px; white-space: nowrap;
  }
  .label--dark .slogan { color: var(--snow); }
  .label--light .slogan { color: var(--charcoal); }

  .net-weight {
    position: absolute; left: 0; right: 0; text-align: center;
    font-family: "Open Sans", sans-serif; font-size: 14px;
  }
  .label--dark .net-weight { top: 433px; color: #9a9a9a; }
  .label--light .net-weight { top: 435px; color: var(--ink); }
</style>
</head>
<body>
<div class="canvas">

  <section class="label label--dark">
    <div class="botanical-wreath" role="img" aria-label="Line-drawn wild flowers, peonies, tulips and crescent moons in pale grey framing the name"></div>
    <h1 class="brand-plate">Thornmoor Stillhouse</h1>
    <div class="slogan-row">
      <span class="rule rule--left"></span>
      <span class="slogan">Crafted with Magic</span>
      <span class="rule rule--right"></span>
    </div>
    <p class="net-weight">70 g I 2.4 oz</p>
  </section>

  <section class="label label--light">
    <div class="botanical-wreath" role="img" aria-label="Line-drawn wild flowers, peonies, tulips and crescent moons in dark grey framing the name"></div>
    <h2 class="brand-plate">Thornmoor Stillhouse</h2>
    <div class="slogan-row">
      <span class="rule"></span>
      <span class="slogan">Crafted with Magic</span>
      <span class="rule"></span>
    </div>
    <p class="net-weight">70 g I 2.4 oz</p>
  </section>

</div>
</body>
</html>
```